Cradlecraft by Lorna Business Card Design

i am starting a new business as a reborn artist (that is painting dolls to make them look like real live babies)

i eventually want to sell the dolls that i make and have classed in reborning. but at the moment i just want to get my name out there.

I do not currently have images of the dolls so cannot have an image in the design.

Non compulsory thoughts: i like the look of old wood, white and baby pink,even hot pink, and lace, denim. i had in mind something like a tiny baby in a old cradle or something, a old drawer, box, something different or unusual, it has to be a girl baby. i am also open to other thoughts on the matter. i would like plain writing not all swirly
Updates

Sorry to change but would like it to read country cradlecraft by lorna.

Industry/Entity Type

Painting

Contact Information for Business Card

Cradlecraft by Lorna
little darlings that never grow up
Reborn Artist Lorna Whitby
0431 756 842
marlo.t@quillbox.com

```html
<!DOCTYPE html>
<html lang="en">
<head>
<meta charset="utf-8">
<title>Cradlecraft by Lorna – Business Card</title>
<link rel="stylesheet" href="https://fonts.googleapis.com/css2?family=Didact+Gothic&family=Source+Sans+3:wght@400;600;700&display=swap">
<style>
  :root {
    --page-bg: #f4f4f4;
    --lace-light: #fbe6f0;
    --lace-mid: #f3c9dd;
    --lace-deep: #eab3cd;
    --hot-pink: #e0338b;
    --hot-pink-light: #ec6aa9;
    --name-pink: #f27fbb;
    --brand-brown: #3a2417;
    --tagline-ink: #3b2331;
    --wood-dark: #4f2a16;
    --wood-mid: #6b3a20;
    --wood-light: #7d4628;
    --cradle-brown: #8a4a2c;
    --baby-pink: #f2c6d3;
    --white: #ffffff;
  }

  html, body {
    margin: 0;
    width: 1200px;
    height: 900px;
    overflow: hidden;
    background: var(--page-bg);
  }

  .card {
    position: absolute;
    left: 100px;
    top: 160px;
    width: 1000px;
    height: 580px;
    border-radius: 38px;
    overflow: hidden;
    box-shadow: 0 10px 30px rgba(0, 0, 0, 0.12);
  }

  .card__lace {
    position: absolute;
    inset: 0 0 290px 0;
    background:
      radial-gradient(ellipse at 30% 40%, var(--lace-light) 0%, transparent 55%),
      radial-gradient(ellipse at 80% 70%, var(--lace-light) 0%, transparent 50%),
      linear-gradient(135deg, var(--lace-mid), var(--lace-deep) 50%, var(--lace-mid));
  }

  .card__cradle-photo {
    position: absolute;
    left: 70px;
    top: 40px;
    width: 300px;
    height: 240px;
    border-radius: 10px;
    background:
      radial-gradient(ellipse at 45% 30%, var(--baby-pink) 0%, transparent 40%),
      linear-gradient(180deg, #b86a44 0%, var(--cradle-brown) 60%, #6e371f 100%);
  }

  .brand {
    position: absolute;
    left: 390px;
    top: 118px;
    width: 580px;
    margin: 0;
    font-family: "Source Sans 3", sans-serif;
    font-weight: 600;
    font-size: 50px;
    color: var(--brand-brown);
    text-align: center;
    line-height: 1;
    white-space: nowrap;
  }

  .card__band {
    position: absolute;
    left: 0;
    right: 0;
    top: 290px;
    height: 42px;
    background: linear-gradient(180deg, var(--hot-pink-light), var(--hot-pink) 45%);
    display: flex;
    align-items: center;
    justify-content: center;
  }
  .tagline {
    margin: 0;
    font-family: "Didact Gothic", sans-serif;
    font-size: 22px;
    letter-spacing: 14px;
    color: var(--tagline-ink);
    white-space: nowrap;
  }

  .card__wood {
    position: absolute;
    left: 0;
    right: 0;
    top: 332px;
    bottom: 0;
    background: linear-gradient(90deg, var(--wood-mid), var(--wood-light) 35%, var(--wood-mid) 60%, var(--wood-dark) 100%);
  }

  .contact {
    position: absolute;
    left: 0;
    right: 0;
    top: 352px;
    text-align: center;
    font-family: "Source Sans 3", sans-serif;
    color: var(--white);
    padding-right: 60px;
  }
  .contact__name {
    margin: 0;
    font-size: 36px;
    font-weight: 700;
    color: var(--name-pink);
    line-height: 1.1;
  }
  .contact__role {
    margin: 4px 0 0;
    font-size: 23px;
    font-weight: 400;
  }
  .contact__phone {
    margin: 30px 0 0;
    font-size: 30px;
    font-weight: 600;
    line-height: 1.1;
  }
  .contact__email {
    margin: 2px 0 0;
    font-size: 31px;
    font-weight: 600;
  }
</style>
</head>
<body>
  <article class="card">
    <div class="card__lace" role="img" aria-label="Pink lace texture background"></div>
    <div class="card__cradle-photo" role="img" aria-label="Photo of a baby girl in a pink outfit sitting in an old wooden rocking cradle"></div>

    <h1 class="brand">Cradlecraft by Lorna</h1>

    <div class="card__band">
      <p class="tagline">little darlings that never grow up</p>
    </div>

    <div class="card__wood" role="img" aria-label="Dark wood grain texture"></div>

    <section class="contact">
      <h2 class="contact__name">Lorna Whitby</h2>
      <p class="contact__role">Reborn Artist</p>
      <p class="contact__phone">0431 756 842</p>
      <p class="contact__email">marlo.t@quillbox.com</p>
    </section>
  </article>
</body>
</html>
```